Kestrel.vc needs a better website design!

We need a new and better website for Kestrel.vc. We're a Canadian venture capital firm that invests in innovative entrepreneurs. We compete against the following websites: lumora.vc, brightvalefund.ca, osprovc.com, and tessara.vc. We're a diverse group of partners and we're dedicated to the founders we invest in.
Updates

I don’t really like stock photos of random people as part of the website design…so please try to stay away from using those images. Thanks, Owen

Target Market(s)

Canadian entrepreneurs and investors

Industry/Entity Type

Venture capital, finance, investment, entrepreneurship

Coding

Coded - Design and coding required

Number of Pages Required

4 page

Font styles to use
Sans Serif

Colors

Designer to choose colors to be used in the design.

Requirements
Must have
• Clean crisp overall design. Fast and to the point.
Nice to have
• Check out www.kestrel.vc - I did it myself and it is too basic and too wordy.
Should not have
• No stock images with random people in them! Not too wordy or with too many large images that are slow to load.

```html
<!DOCTYPE html>
<html lang="en">
<head>
<meta charset="utf-8">
<title>Kestrel.vc — Canadian Venture Capital</title>
<link rel="stylesheet" href="https://fonts.googleapis.com/css2?family=Poppins:wght@300;400;500;600;700&display=swap">
<style>
:root{
  --green:#7c9a38;
  --green-dark:#6b8a2c;
  --ink:#1f1f1f;
  --muted:#5d5d5d;
  --line:#e8e8e8;
  --panel:#f1f1f1;
  --footer:#252525;
  --footer-bottom:#1b1b1b;
  --white:#ffffff;
}
*{box-sizing:border-box;margin:0;padding:0}
html,body{width:1200px;height:3256px;overflow:hidden}
body{position:relative;font-family:"Poppins",sans-serif;color:var(--ink);background:var(--white)}
.abs{position:absolute}
.accent{color:var(--green)}

/* header */
.site-header{position:absolute;left:0;top:0;width:1200px;height:88px}
.brand{position:absolute;left:88px;top:16px;display:flex;align-items:center;gap:12px}
.brand-dot{width:56px;height:56px;border-radius:50%;border:3px solid var(--green)}
.brand-name{font-size:26px;font-weight:600;color:var(--green);letter-spacing:1px}
.main-nav{position:absolute;left:550px;top:36px;display:flex;gap:25px;font-size:12.5px;font-weight:500;text-transform:uppercase}
.main-nav a{color:var(--ink);text-decoration:none}
.main-nav a.active{color:var(--green);position:relative}
.main-nav a.active::before{content:"";position:absolute;left:-8px;right:-8px;top:-36px;height:3px;background:var(--green)}
.search-icon{position:absolute;left:940px;top:34px}
.contact-btn{position:absolute;left:994px;top:27px;width:116px;height:34px;border:1.5px solid var(--ink);font-size:11.5px;font-weight:600;display:flex;align-items:center;justify-content:center;text-transform:uppercase}

/* hero */
.hero-title{left:86px;top:182px;font-size:47px;font-weight:700;line-height:55px;letter-spacing:-.5px}
.hero-sub{left:86px;top:360px;font-size:22px;font-weight:400}
.scroll-cue{left:84px;top:462px;width:26px;display:flex;flex-direction:column;align-items:center;gap:10px}
.scroll-cue span{writing-mode:vertical-rl;transform:rotate(180deg);font-size:10px;font-weight:500;letter-spacing:.5px}
.mouse{width:20px;height:30px;border:2px solid var(--ink);border-radius:10px;position:relative}
.mouse::after{content:"";position:absolute;left:7px;top:6px;width:2px;height:7px;background:var(--ink);border-radius:1px}
.green-band{left:0;top:618px;width:1200px;height:432px;background:var(--green)}
.band-circle{left:228px;top:556px;width:128px;height:128px;border-radius:50%;background:rgba(255,255,255,.55);clip-path:inset(62px 0 0 0)}
.hero-photo{left:582px;top:88px;width:618px;height:578px;background:linear-gradient(135deg,#cfd3d6 0%,#a08b7a 45%,#6e5a4c 75%,#d8d8d8 100%);box-shadow:0 30px 50px rgba(0,0,0,.22)}
.band-mark{left:572px;top:752px;width:56px;height:56px;border-radius:50%;border:3px solid var(--white)}
.band-text{left:100px;top:828px;width:1000px;text-align:center;color:var(--white);font-size:28px;font-weight:400;line-height:43px}
.band-text b{font-weight:700;font-size:32px}

/* section titles */
.section-title{left:0;width:1200px;text-align:center;font-size:33px;font-weight:600;line-height:41px}
.section-sub{left:0;width:1200px;text-align:center;font-size:16px;color:var(--muted)}

/* criteria */
.criteria-card{top:1264px;width:253px;height:271px;background:var(--white);box-shadow:0 10px 40px rgba(0,0,0,.07);text-align:center;padding-top:36px}
.criteria-card.active{border-bottom:2px solid var(--green)}
.criteria-card svg{display:block;margin:0 auto}
.criteria-card h3{font-size:14.5px;font-weight:600;margin-top:26px}
.criteria-card p{font-size:13px;color:var(--muted);line-height:20px;margin:20px 24px 0}

/* portfolio */
.portfolio-photo{left:88px;top:1754px;width:638px;height:460px;background:linear-gradient(120deg,#e4e6e5 0%,#9ea7ab 40%,#c9c4bb 70%,#eceae6 100%)}
.portfolio-panel{left:729px;top:1754px;width:381px;height:460px;background:var(--panel);text-align:center}
.company-name{margin-top:70px;font-size:38px;font-weight:600;color:var(--ink);display:flex;align-items:center;justify-content:center;gap:10px}
.company-name i{width:14px;height:14px;background:var(--green);border-radius:50%}
.company-desc{margin:22px 48px 0;font-size:14.5px;line-height:22.5px;color:var(--muted)}
.arrow-btn{top:2100px;width:60px;height:60px;border-radius:50%;background:#e4e4e4;display:flex;align-items:center;justify-content:center}

/* team */
.team-card{top:2409px;width:246px;height:320px;background:var(--white);box-shadow:0 10px 40px rgba(0,0,0,.07);text-align:center;padding-top:40px}
.avatar{width:110px;height:110px;border-radius:50%;margin:0 auto;background:linear-gradient(160deg,#e3e3e3,#c8c8c8)}
.team-card h3{font-size:16px;font-weight:600;margin-top:24px}
.team-card .role{font-size:12.5px;color:#888;margin-top:4px}
.team-card p{font-size:13.5px;color:var(--muted);line-height:20.5px;margin:16px 22px 0}

/* footer */
.site-footer{left:0;top:2841px;width:1200px;height:415px;background:var(--footer);color:var(--white)}
.footer-brand{left:0;top:70px;width:1200px;display:flex;flex-direction:column;align-items:center;gap:14px}
.footer-brand .brand-dot{width:80px;height:80px}
.footer-brand .brand-name{font-size:26px}
.footer-nav{left:0;top:222px;width:1200px;display:flex;justify-content:center;gap:28px;font-size:14.5px;font-weight:500;text-transform:uppercase}
.social{left:0;top:259px;width:1200px;display:flex;justify-content:center;gap:9px}
.social span{width:33px;height:33px;border-radius:50%;border:1.5px solid #5a5a5a;background:#333}
.footer-bottom{left:0;top:358px;width:1200px;height:57px;background:var(--footer-bottom);font-size:13px;font-weight:500;display:flex;align-items:center;justify-content:center}
.to-top{left:1082px;top:3160px;width:58px;height:58px;border-radius:50%;background:var(--green);display:flex;align-items:center;justify-content:center}
</style>
</head>
<body>

<header class="site-header">
  <div class="brand"><span class="brand-dot"></span><span class="brand-name">KESTREL.VC</span></div>
  <nav class="main-nav">
    <a class="active" href="#">Home</a><a href="#">Team</a><a href="#">Companies</a><a href="#">What we look for</a>
  </nav>
  <svg class="search-icon" width="18" height="18" viewBox="0 0 18 18" fill="none" stroke="#1f1f1f" stroke-width="1.6"><circle cx="7.5" cy="7.5" r="5.5"/><path d="M11.5 11.5L16 16"/></svg>
  <div class="contact-btn">Contact us</div>
</header>

<section class="hero">
  <div class="abs green-band"></div>
  <div class="abs band-circle"></div>
  <h1 class="abs hero-title">We're a <span class="accent">canadian</span><br>venture capital firm<br>that <span class="accent">invests</span></h1>
  <p class="abs hero-sub">In innovative entrepreneurs.</p>
  <div class="abs scroll-cue"><span>SCROLL</span><div class="mouse"></div></div>
  <div class="abs hero-photo" role="img" aria-label="Photo of three colleagues reviewing documents at a desk"></div>
  <span class="abs band-mark"></span>
  <p class="abs band-text">Kestrel.vc is a venture capital firm that <b>invests</b> in innovative seed-stage <b>technology</b> companies in Western Canada focused on B2B and SaaS markets.</p>
</section>

<section class="criteria">
  <h2 class="abs section-title" style="top:1153px">What <span class="accent">we're</span> looking for</h2>
  <p class="abs section-sub" style="top:1208px">We invest in innovative technology companies with these characteristics:</p>

  <div class="abs criteria-card" style="left:207px">
    <svg width="80" height="74" viewBox="0 0 80 74" fill="none" stroke="#1f1f1f" stroke-width="2.2">
      <circle cx="40" cy="10" r="7"/><path d="M29 28a11 11 0 0 1 22 0z" fill="#7c9a38"/>
      <circle cx="14" cy="46" r="7"/><path d="M2 70a12 12 0 0 1 24 0z"/>
      <circle cx="40" cy="44" r="6"/><path d="M30 66a10 10 0 0 1 20 0z"/>
      <circle cx="66" cy="46" r="7"/><path d="M54 70a12 12 0 0 1 24 0z"/>
      <path d="M40 30v6M22 40l12-6M58 40l-12-6"/>
    </svg>
    <h3>Founding Team</h3>
    <p>Visionary, Committed, Coachable, Skilled, Aligned, With Market Fit</p>
  </div>

  <div class="abs criteria-card active" style="left:474px">
    <svg width="80" height="74" viewBox="0 0 80 74" fill="none" stroke="#1f1f1f" stroke-width="2.2">
      <path d="M24 2h26l12 12v58H24z"/><path d="M50 2v12h12"/>
      <circle cx="36" cy="36" r="14" fill="#fff"/><path d="M36 36V22a14 14 0 0 1 14 14z" fill="#7c9a38"/><path d="M36 36h14a14 14 0 0 1-25 8z" fill="#7c9a38"/>
    </svg>
    <h3>Total Addressable Market</h3>
    <p>Large, Growing, and Attractive; With a Manageable Competitive Landscape</p>
  </div>

  <div class="abs criteria-card" style="left:741px">
    <svg width="80" height="74" viewBox="0 0 80 74" fill="none" stroke="#1f1f1f" stroke-width="2.2">
      <rect x="4" y="4" width="70" height="44"/><path d="M10 48v20h34" stroke-dasharray="3 3"/>
      <path d="M36 40V20M28 28l8-8 8 8"/>
      <path d="M48 52h8a4 4 0 0 1 8 0h8v16H48z" fill="#7c9a38"/>
    </svg>
    <h3>Product Market Fit</h3>
    <p>MVP + Initial Market Validation; Early Revenue and Growth Potential</p>
  </div>
</section>

<section class="portfolio">
  <h2 class="abs section-title" style="top:1640px">Check out our <span class="accent">innovative</span> our<br>portfolio companies!</h2>
  <div class="abs portfolio-photo" role="img" aria-label="Photo of a team meeting around a table behind a glass wall"></div>
  <div class="abs portfolio-panel">
    <div class="company-name"><i></i>tallyflow</div>
    <p class="company-desc">Tallyflow has developed groundbreaking cash flow forecasting software designed to address critical cash flow risks for accounting professionals, finance managers, decision makers, and business owners.</p>
  </div>
  <div class="abs arrow-btn" style="left:852px"><svg width="22" height="14" viewBox="0 0 22 14" fill="none" stroke="#1f1f1f" stroke-width="1.6"><path d="M21 7H2M8 1L2 7l6 6"/></svg></div>
  <div class="abs arrow-btn" style="left:925px"><svg width="22" height="14" viewBox="0 0 22 14" fill="none" stroke="#1f1f1f" stroke-width="1.6"><path d="M1 7h19M14 1l6 6-6 6"/></svg></div>
</section>

<section class="team">
  <h2 class="abs section-title" style="top:2309px">Meet <span class="accent">the</span> team</h2>
  <p class="abs section-sub" style="top:2353px">We are serial entrepreneurs and venture capital investors who provide:</p>

  <div class="abs team-card" style="left:88px">
    <div class="avatar" role="img" aria-label="Illustrated portrait of Owen Hartley"></div>
    <h3>Owen Hartley</h3><div class="role">Partner</div>
    <p>Owen is an experienced entrepreneur and successful investor. He started…</p>
  </div>
  <div class="abs team-card" style="left:348px">
    <div class="avatar" role="img" aria-label="Illustrated portrait of Ravi Menon"></div>
    <h3>Ravi Menon</h3><div class="role">Partner</div>
    <p>Ravi is a serial entrepreneur and angel investor. He served…</p>
  </div>
  <div class="abs team-card" style="left:607px">
    <div class="avatar" role="img" aria-label="Illustrated portrait of Elena Fischer"></div>
    <h3>Elena Fischer</h3><div class="role">Partner</div>
    <p>Elena is the former president of Northgate Angels, one of Canada's most…</p>
  </div>
  <div class="abs team-card" style="left:865px">
    <div class="avatar" role="img" aria-label="Illustrated portrait of Jordan Blake"></div>
    <h3>Jordan Blake</h3><div class="role">Advisor</div>
    <p>Jordan is the newly appointed CEO of LedgerPoint and is also a Director…</p>
  </div>
</section>

<footer class="abs site-footer">
  <div class="abs footer-brand"><span class="brand-dot"></span><span class="brand-name">KESTREL.VC</span></div>
  <nav class="abs footer-nav"><span>Home</span><span>Team</span><span>Companies</span><span>What we look for</span><span>Contact us</span></nav>
  <div class="abs social"><span></span><span></span><span></span><span></span></div>
  <div class="abs footer-bottom">Copyright © 2021 Kestrel.vc - All Rights Reserved</div>
</footer>
<div class="abs to-top"><svg width="14" height="20" viewBox="0 0 14 20" fill="none" stroke="#fff" stroke-width="1.6"><path d="M7 19V2M1 8l6-6 6 6"/></svg></div>

</body>
</html>
```